Career development coaching - school lever to adults, needs a business card

Tandem Lark - An independent Career Advice business that provides 1-2-1 advice,for career development, entrepreneurial support and workshops needs a business card. Our clients of all ages (school leaver to adults looking for a career move) and universities and colleges. We would like the card to be double-sided with a modern, professional look. Looking for something professional yet very creative and original. Want a standard size business card that inspires a second look because it stands out from the rest.

One side of the card to have a design incorporating the logo with Tandem Lark name with the strap line “Helping you find your future” and space for the company website

Other side of the card to the logo/Tandem Lark name and the usual contact information:
Individual Name
Job Title (for example, Director)
Phone number
Email address
Company website address

Facebook, LinkedIn and Twitter links will need to go somewhere (back or front!)

The design will be used for 3 individuals so should be editable so that we can update as needed/as we grow.

Attached is the company logo/colours to be incorporated.

Target Market(s)

1-2-1 advice,for career development, entrepreneurial support and workshops needs a business card. Our clients of all ages (school leaver to adults looking for a career move) and universities and colleges.

Industry/Entity Type

Consulting

Contact Information for Business Card

Individual Name
Phone number
Email address
Company website address

Font styles to use
Sans Serif

Colors
0255a3
3176b5
faa54b
f78f20
85acd3
cfdeed

Requirements
Must have
• use the Tandem Lark Logo in some way - using the colours and the blue/orange palette
• For the logo - hope this makes sense to someone or if they direclty relate to the logo image attached!
• For the Orange:- Pantone 1585 C
• In CMYK : C3 M71 Y100 K0
• For the Blue:- 100% Pantone 7469 C
• In CMYK : C100 M62 Y27 K7
• Please feel free to contact me with any questions for more info
Nice to have
• happy to see any creative designs
Should not have
• Nothing too traditional,

```html
<!DOCTYPE html>
<html lang="en">
<head>
<meta charset="utf-8">
<title>Tandem Lark – Business Card</title>
<link href="https://fonts.googleapis.com/css2?family=Montserrat:wght@400;500;600&display=swap" rel="stylesheet">
<style>
  :root {
    --blue: #075a8c;
    --blue-text: #0b5f8e;
    --orange: #f47b20;
    --white: #ffffff;
    --stage: #e9ecef;
    --ink-soft: #2a5f85;
  }
  * { box-sizing: border-box; margin: 0; padding: 0; }
  html, body { width: 1200px; height: 900px; overflow: hidden; }
  body {
    background: var(--stage);
    font-family: "Montserrat", Arial, sans-serif;
    position: relative;
  }
  .card {
    position: absolute;
    left: 260px;
    width: 680px;
    height: 388px;
    border-radius: 22px;
    overflow: hidden;
    box-shadow: 0 8px 24px rgba(0,0,0,.18);
  }
  /* Front side */
  .card-front {
    top: 40px;
    background: var(--blue);
    color: var(--white);
    display: flex;
    flex-direction: column;
    align-items: center;
    justify-content: center;
    text-align: center;
  }
  .brand-mark {
    width: 96px; height: 96px;
    border-radius: 50%;
    border: 14px solid var(--white);
    margin-bottom: 22px;
  }
  .front-name {
    font-weight: 600;
    font-size: 38px;
    letter-spacing: 3px;
    text-transform: uppercase;
    color: var(--white);
  }
  .tagline {
    margin-top: 10px;
    font-size: 17px;
    font-weight: 500;
    letter-spacing: 2px;
    text-transform: uppercase;
  }
  .front-web {
    margin-top: 12px;
    font-size: 18px;
    letter-spacing: 1px;
  }
  .front-web .accent { color: var(--orange); font-weight: 600; }

  /* Back side */
  .card-back {
    top: 472px;
    background: var(--white);
  }
  .back-band { position: absolute; left: 0; top: 0; width: 680px; height: 388px; }
  .back-name {
    position: absolute;
    right: 40px; top: 48px;
    font-weight: 600;
    font-size: 44px;
    letter-spacing: 3px;
    text-transform: uppercase;
    color: var(--blue-text);
  }
  .person {
    position: absolute;
    right: 40px; top: 118px;
    text-align: right;
  }
  .person-name { color: var(--orange); font-size: 26px; font-weight: 600; line-height: 1.1; }
  .person-title { color: var(--ink-soft); font-size: 15px; margin-top: 2px; }
  .contacts {
    position: absolute;
    right: 40px; top: 196px;
    list-style: none;
    text-align: right;
  }
  .contacts li {
    display: flex;
    justify-content: flex-end;
    align-items: center;
    gap: 10px;
    font-size: 16px;
    line-height: 25px;
    color: var(--ink-soft);
  }
  .contacts .accent { color: var(--orange); font-weight: 600; }
  .icon { width: 13px; height: 13px; flex: none; }
  .dot { width: 9px; height: 9px; border-radius: 50%; background: var(--blue-text); margin: 0 2px; flex: none; }
</style>
</head>
<body>

<section class="card card-front">
  <div class="brand-mark" aria-hidden="true"></div>
  <h1 class="front-name">Tandem Lark</h1>
  <p class="tagline">Helping you find your future</p>
  <p class="front-web">www.<span class="accent">tandemlark</span>.com</p>
</section>

<section class="card card-back">
  <svg class="back-band" viewBox="0 0 680 388" aria-hidden="true">
    <path d="M0 0 H48 C70 130 140 260 200 388 H0 Z" fill="#075a8c"/>
    <path d="M58 0 H70 C92 130 160 260 222 388 H208 C146 262 78 130 58 0 Z" fill="#f47b20"/>
    <circle cx="128" cy="122" r="62" fill="#ffffff" stroke="#075a8c" stroke-width="10"/>
  </svg>

  <h2 class="back-name">Tandem Lark</h2>

  <div class="person">
    <p class="person-name">Mara Ellison</p>
    <p class="person-title">Director</p>
  </div>

  <ul class="contacts">
    <li>+330 5128-4093
      <svg class="icon" viewBox="0 0 16 16"><path d="M4 1 L6.5 4.5 5 6.5 C6 8.5 7.5 10 9.5 11 L11.5 9.5 15 12 13.5 15 C7 14.5 1.5 9 1 2.5 Z" fill="#0b5f8e"/></svg>
    </li>
    <li>info@tandemlark.com
      <svg class="icon" viewBox="0 0 16 16"><rect x="1" y="3" width="14" height="10" fill="none" stroke="#0b5f8e" stroke-width="1.6"/><path d="M1 3 L8 9 15 3" fill="none" stroke="#0b5f8e" stroke-width="1.6"/></svg>
    </li>
    <li><span>www.<span class="accent">tandemlark</span>.com</span>
      <svg class="icon" viewBox="0 0 16 16"><circle cx="8" cy="8" r="6.5" fill="none" stroke="#0b5f8e" stroke-width="1.5"/><ellipse cx="8" cy="8" rx="3" ry="6.5" fill="none" stroke="#0b5f8e" stroke-width="1.2"/><path d="M1.5 8 H14.5" stroke="#0b5f8e" stroke-width="1.2"/></svg>
    </li>
    <li>tandemlark.com <span class="dot"></span></li>
    <li>@tandemlark.com <span class="dot"></span></li>
    <li>@tandemlark.com <span class="dot"></span></li>
  </ul>
</section>

</body>
</html>
```